App Design - Job Poise Lantern

We require an App Design for our new App called 'Poise Lantern'. This app is essentially an assistant to help Users prepare for job interviews, to help them get hired. <br/><br/>Users who download the App can view common Questions and Answers, save their favourite responses and also view common Interview Tips. <br/><br/>The vision for our App is for Users who are preparing for an interview (1 week before, 1 day before, even 1 hour before), are able to download, view and educate themselves on common questions and responses, and then be confident to land the job. <br/><br/>Our team has developed wireframes to help highlight what each screen should do and include. Please see attached document, which also highlights key requirements for the experience. Feel free to add/remove/edit what you see on these wireframes. Our preference is that you use Adobe XD please.<br/><br/>In terms of design guidelines, we want the experience to be simple, intuitive and 'memorable' to help Users to remember the questions/responses when they are in the interview. <br/><br/>The final design should communicate 'neat and clean professionalism'; we like the design of: vocatia hub com au<br/><br/>Thank you for reading! Good luck !

Target Market(s)

Professional job seekers

Font styles to use
Sans Serif

Colors

Designer to choose colors to be used in the design.

Requirements
Must have
• Please see my PixelBazaar_UX file that I have uploaded
Nice to have
• Could you also please include some ideas on how we can incorporate Advertising into the app screens

```html
<!DOCTYPE html>
<html lang="en">
<head>
<meta charset="utf-8">
<title>Poise Lantern – App Design</title>
<link href="https://fonts.googleapis.com/css2?family=Outfit:wght@500;600;700&family=Figtree:wght@400;500;600;700&display=swap" rel="stylesheet">
<style>
:root{
  --cyan:#00dcf5;
  --sky:#a6eef9;
  --pill:#a2ebf8;
  --blob:#a0eef8;
  --ink:#2b3445;
  --grey:#878d97;
  --mute:#b7bbc2;
  --panel:#f4f4f5;
  --line:#ececee;
  --pink:#f8cbdd;
}
*{box-sizing:border-box;margin:0;padding:0}
html,body{width:1200px;height:1200px;overflow:hidden;background:#fff}
.board{position:relative;width:1200px;height:1200px;overflow:hidden;background:#fff;font-family:"Figtree",sans-serif;color:var(--ink)}
.blob{position:absolute;left:0;top:0}
.brand{position:absolute;left:89px;top:118px;display:flex;align-items:center;gap:14px}
.brand-dot{width:36px;height:36px;border-radius:50%;background:var(--cyan)}
.brand-name{font-family:"Outfit",sans-serif;font-weight:700;font-size:31px;color:var(--ink);letter-spacing:.2px}

.phone{position:absolute;width:174px;height:370px;border:4px solid var(--ink);border-radius:24px;background:#fff;overflow:hidden;display:flex;flex-direction:column}
.top{top:229px}.bottom{top:707px}

.status{display:flex;justify-content:space-between;align-items:center;height:14px;padding:3px 10px 0;font-size:5px;font-weight:600;flex:none}
.status svg{width:24px;height:5px}
.bar{display:flex;align-items:center;justify-content:space-between;height:27px;padding:0 9px;flex:none}
.bar .i{width:9px;height:9px;color:var(--ink)}
.bar .bm{width:6px;height:8px;color:var(--ink)}
.bar .ghost{width:9px}
.pill-title{background:var(--pill);border-radius:10px;padding:4px 11px;font-size:5.2px;font-weight:600}
.search{flex:1;margin:0 8px 0 0;background:var(--panel);border-radius:3px;height:16px;display:flex;align-items:center;gap:3px;padding:0 6px;font-size:4.6px;color:var(--mute)}
.search svg{width:6px;height:6px;color:var(--mute)}
.search.wide{margin:0 9px;flex:none;height:16px}

.gray{background:var(--panel)}
.fill{flex:1}
.hint{font-size:5px;color:var(--grey);padding:9px 9px 7px;font-weight:500}
.intro{font-size:5.3px;color:var(--grey);line-height:1.55;padding:10px 9px 8px}
.intro b{color:var(--ink);font-weight:700}
.sec-h{font-size:8.5px;font-weight:600;padding:10px 9px 5px;display:flex;align-items:center;gap:4px}
.sec-h .dia{width:5px;height:5px;background:var(--cyan);transform:rotate(45deg);border-radius:1px}

.row{display:flex;align-items:center;gap:6px;padding:6px 9px;border-bottom:1px solid var(--line);background:#fff}
.ico{width:15px;height:15px;border-radius:50%;background:var(--sky);flex:none}
.row-txt{flex:1;min-width:0}
.row-t{font-size:6.4px;font-weight:600}
.row-d{font-size:3.3px;color:var(--grey);white-space:nowrap;overflow:hidden}
.chev{width:4px;height:6px;color:var(--mute);flex:none}

.cat{display:flex;align-items:center;gap:7px;padding:8px 9px;background:#fff;border-bottom:1px solid var(--line)}
.thumb{width:32px;height:30px;border-radius:4px;background:linear-gradient(135deg,#d5f7fc,var(--sky));flex:none}
.cat-t{font-size:6.8px;font-weight:600;margin-bottom:2px}
.cat-d{font-size:3.3px;color:var(--grey);line-height:1.4}

.card{background:#fff;padding:8px 9px 9px;margin-top:5px}
.meta{font-size:3.2px;color:var(--grey);text-transform:uppercase;margin-bottom:4px;letter-spacing:.1px}
.q{font-size:5.5px;font-weight:600;line-height:1.6}
.chips{display:flex;gap:4px;margin-top:5px}
.chip{font-size:3.7px;border-radius:6px;padding:2px 5px;display:inline-flex;gap:2px;align-items:center;background:#fff;box-shadow:0 0 0 .6px #e4e5e8;font-weight:600}
.chip svg{width:3.5px;height:4px}
.chip.save{background:var(--sky);box-shadow:none}
.chip.del{background:var(--pink);box-shadow:none;color:#c4406f}
.faded{opacity:.35}

.head{display:flex;align-items:center;gap:6px;padding:6px 9px 8px;font-size:7.6px;font-weight:600;background:#fff;flex:none}
.head .ico{width:14px;height:14px}
.sortzone{padding:8px 9px 10px;flex:none}
.sort{background:var(--ink);color:#fff;font-size:4.8px;font-weight:600;padding:3px 7px;border-radius:8px;display:inline-block}
.qi{background:#fff;padding:9px 9px 8px;margin-bottom:4px}
.view{display:inline-block;font-size:3.7px;font-weight:600;padding:2px 5px;border-radius:6px;box-shadow:0 0 0 .6px #e4e5e8;margin-top:4px}

.open{background:#fff;padding:9px 8px 8px;display:flex;align-items:flex-start;gap:4px;margin-bottom:5px}
.nav{font-size:3px;color:var(--mute);text-align:center;width:12px;flex:none;padding-top:7px}
.nav.next{color:var(--cyan)}
.open-mid{flex:1;text-align:center}
.open .q{font-size:5.4px}
.resp{background:#fff;margin:0 7px 6px;padding:8px 10px}
.resp-h{display:flex;justify-content:space-between;font-size:5.4px;font-weight:600}
.resp-h svg{width:4px;height:5px;color:var(--ink)}
.tick{width:8px;height:1.5px;background:var(--cyan);margin:3px 0 6px;border-radius:1px}
.resp p{font-size:4.2px;color:var(--grey);line-height:1.7}

.land-logo{display:flex;justify-content:center;align-items:center;gap:4px;margin-top:40px;font-family:"Figtree",sans-serif;font-weight:700;font-size:10.5px}
.land-logo span.d{width:11px;height:11px;border-radius:50%;background:var(--cyan)}
.land-art{width:122px;height:100px;margin:46px auto 0;border-radius:45% 50% 40% 48%;background:linear-gradient(160deg,#dff9fd,var(--blob))}
.land-t{text-align:center;font-size:6.6px;font-weight:700;margin-top:22px}
.land-d{text-align:center;font-size:5px;color:var(--grey);line-height:1.65;margin-top:3px;padding:0 20px}
.land-d b{color:var(--ink)}
.cta{margin:33px auto 0;width:146px;height:23px;border-radius:12px;background:var(--cyan);display:flex;align-items:center;justify-content:center;font-size:5.6px;font-weight:700}

.empty-art{width:92px;height:98px;margin:62px auto 0;border-radius:48% 52% 45% 50%;background:linear-gradient(150deg,#c9f4fb,var(--blob))}
.empty-t{text-align:center;font-size:6.5px;color:var(--grey);line-height:1.6;margin-top:14px;padding:0 20px;font-weight:500}

.label{position:absolute;width:240px;text-align:center;font-family:"Outfit",sans-serif;font-weight:600;font-size:12.5px;line-height:1.25;color:var(--ink)}
.label .sub{color:#9ba1a9}
</style>
</head>
<body>
<div class="board">

  <svg class="blob" width="1200" height="1200" viewBox="0 0 1200 1200" aria-hidden="true">
    <path d="M661 0H1200V523C1100 520 1030 470 990 380C955 300 900 230 820 170C760 120 700 70 661 0Z" fill="var(--blob)"/>
  </svg>

  <div class="brand"><span class="brand-dot"></span><span class="brand-name">Poise Lantern</span></div>

  <!-- Landing -->
  <div class="phone top" style="left:85px">
    <div class="land-logo"><span class="d"></span>Poise Lantern</div>
    <div class="land-art" role="img" aria-label="Illustration of a job seeker with binoculars looking at city buildings"></div>
    <div class="land-t">Job Interview Questions</div>
    <div class="land-d">Your guide to the most common interview questions, and the best responses to <b>help you get hired!</b></div>
    <div class="cta">Get started</div>
  </div>

  <!-- Menu -->
  <div class="phone top" style="left:299px">
    <div class="status"><span>9:41</span><svg viewBox="0 0 24 5"><rect x="0" y="3" width="1" height="2" fill="#2b3445"/><rect x="1.6" y="2" width="1" height="3" fill="#2b3445"/><rect x="3.2" y="1" width="1" height="4" fill="#2b3445"/><rect x="4.8" y="0" width="1" height="5" fill="#2b3445"/><path d="M8.5 2a4 4 0 0 1 5 0M9.5 3.2a2.3 2.3 0 0 1 3 0" stroke="#2b3445" stroke-width=".7" fill="none"/><rect x="16" y=".5" width="6.5" height="4" rx="1" stroke="#2b3445" stroke-width=".5" fill="none"/><rect x="16.8" y="1.2" width="4.8" height="2.6" fill="#2b3445"/></svg></div>
    <div class="bar">
      <div class="search" style="margin-left:18px"><svg viewBox="0 0 10 10"><circle cx="4" cy="4" r="3" stroke="currentColor" stroke-width="1.3" fill="none"/><path d="M6.3 6.3 9 9" stroke="currentColor" stroke-width="1.3"/></svg>Search Questions and Tips</div>
      <svg class="bm" viewBox="0 0 8 10"><path d="M1 0h6v10L4 7.5 1 10z" fill="currentColor"/></svg>
    </div>
    <div class="gray fill">
      <div class="intro">We will help you to face job interviews with more <b>confidence!</b> below there's some categories where you can start</div>
      <div class="sec-h" style="padding-top:2px;background:var(--panel)"><span class="dia"></span>Categories</div>
      <div class="cat"><div class="thumb" role="img" aria-label="Illustration of a hand writing on a document"></div><div><div class="cat-t">View Questions &amp; Responses</div><div class="cat-d">Pellentesque quis neque ut sapien fringilla iaculis ege inc...</div></div></div>
      <div class="cat"><div class="thumb" role="img" aria-label="Illustration of a presenter at a board"></div><div><div class="cat-t">Interview Tips</div><div class="cat-d">Pellentesque quis neque ut sapien fringilla iaculis ege inc...</div></div></div>
      <div class="sec-h" style="padding-top:18px">Most searched</div>
      <div class="card">
        <div class="meta">View questions &amp; responses • Behavioural</div>
        <div class="q">Give me an example of a new idea or initiative you have suggested to your manager. How did you implement your idea?</div>
        <div class="chips"><span class="chip save"><svg viewBox="0 0 8 10"><path d="M1 0h6v10L4 7.5 1 10z" fill="#2b3445"/></svg>23 Saves</span><span class="chip">&lt; Share</span></div>
      </div>
      <div class="card faded">
        <div class="meta">View questions &amp; responses • Behavioural</div>
        <div class="q" style="font-weight:500">Give me an example of a new idea or initiative you have suggested to your manager. How did you implement your idea?</div>
      </div>
    </div>
  </div>

  <!-- Selection -->
  <div class="phone top" style="left:517px">
    <div class="status"><span>9:41</span><svg viewBox="0 0 24 5"><rect x="0" y="3" width="1" height="2" fill="#2b3445"/><rect x="1.6" y="2" width="1" height="3" fill="#2b3445"/><rect x="3.2" y="1" width="1" height="4" fill="#2b3445"/><rect x="4.8" y="0" width="1" height="5" fill="#2b3445"/><path d="M8.5 2a4 4 0 0 1 5 0M9.5 3.2a2.3 2.3 0 0 1 3 0" stroke="#2b3445" stroke-width=".7" fill="none"/><rect x="16" y=".5" width="6.5" height="4" rx="1" stroke="#2b3445" stroke-width=".5" fill="none"/><rect x="16.8" y="1.2" width="4.8" height="2.6" fill="#2b3445"/></svg></div>
    <div class="bar"><svg class="i" viewBox="0 0 10 10"><path d="M9 5H1.5M5 1.5 1.5 5 5 8.5" stroke="currentColor" stroke-width="1.3" fill="none"/></svg><span class="pill-title">View Questions &amp; Responses</span><svg class="bm" viewBox="0 0 8 10"><path d="M1 0h6v10L4 7.5 1 10z" fill="currentColor"/></svg></div>
    <div class="gray fill">
      <div class="hint" style="padding-top:16px">Select your question category</div>
      <div class="row"><div class="ico" role="img" aria-label="Behavioural category icon"></div><div class="row-txt"><div class="row-t">Behavioural</div><div class="row-d">Pellentesque quis neque ut sapien fringilla iaculis ege inc...</div></div><svg class="chev" viewBox="0 0 4 6"><path d="M1 .5 3.5 3 1 5.5" stroke="currentColor" stroke-width=".7" fill="none"/></svg></div>
      <div class="row"><div class="ico" role="img" aria-label="Situational category icon"></div><div class="row-txt"><div class="row-t">Situational</div><div class="row-d">Pellentesque quis neque ut sapien fringilla iaculis ege inc...</div></div><svg class="chev" viewBox="0 0 4 6"><path d="M1 .5 3.5 3 1 5.5" stroke="currentColor" stroke-width=".7" fill="none"/></svg></div>
      <div class="row"><div class="ico" role="img" aria-label="Motivational category icon"></div><div class="row-txt"><div class="row-t">Motivational</div><div class="row-d">Pellentesque quis neque ut sapien fringilla iaculis ege inc...</div></div><svg class="chev" viewBox="0 0 4 6"><path d="M1 .5 3.5 3 1 5.5" stroke="currentColor" stroke-width=".7" fill="none"/></svg></div>
      <div class="row"><div class="ico" role="img" aria-label="Technical category icon"></div><div class="row-txt"><div class="row-t">Technical</div><div class="row-d">Pellentesque quis neque ut sapien fringilla iaculis ege inc...</div></div><svg class="chev" viewBox="0 0 4 6"><path d="M1 .5 3.5 3 1 5.5" stroke="currentColor" stroke-width=".7" fill="none"/></svg></div>
      <div class="sec-h" style="padding-top:24px">Most searched</div>
      <div class="card">
        <div class="meta">View questions &amp; responses • Behavioural</div>
        <div class="q">Give me an example of a new idea or initiative you have suggested to your manager. How did you implement your idea?</div>
        <div class="chips"><span class="chip save"><svg viewBox="0 0 8 10"><path d="M1 0h6v10L4 7.5 1 10z" fill="#2b3445"/></svg>23 Saves</span><span class="chip">&lt; Share</span></div>
      </div>
      <div class="card faded">
        <div class="meta">View questions &amp; responses • Behavioural</div>
        <div class="q" style="font-weight:500">Give me an example of a new idea or initiative you have suggested to your manager. How did you implement your idea?</div>
      </div>
    </div>
  </div>

  <!-- View list -->
  <div class="phone top" style="left:731px">
    <div class="status"><span>9:41</span><svg viewBox="0 0 24 5"><rect x="0" y="3" width="1" height="2" fill="#2b3445"/><rect x="1.6" y="2" width="1" height="3" fill="#2b3445"/><rect x="3.2" y="1" width="1" height="4" fill="#2b3445"/><rect x="4.8" y="0" width="1" height="5" fill="#2b3445"/><path d="M8.5 2a4 4 0 0 1 5 0M9.5 3.2a2.3 2.3 0 0 1 3 0" stroke="#2b3445" stroke-width=".7" fill="none"/><rect x="16" y=".5" width="6.5" height="4" rx="1" stroke="#2b3445" stroke-width=".5" fill="none"/><rect x="16.8" y="1.2" width="4.8" height="2.6" fill="#2b3445"/></svg></div>
    <div class="bar"><svg class="i" viewBox="0 0 10 10"><path d="M6.5 1.5 3 5l3.5 3.5" stroke="currentColor" stroke-width="1.3" fill="none"/></svg><span class="pill-title">View Questions &amp; Responses</span><svg class="bm" viewBox="0 0 8 10"><path d="M1 0h6v10L4 7.5 1 10z" fill="currentColor"/></svg></div>
    <div class="head"><div class="ico" role="img" aria-label="Behavioural category icon"></div>Behavioural</div>
    <div class="gray fill">
      <div class="sortzone"><span class="sort">Sort by ⌄</span></div>
      <div class="qi"><div class="q">1. Give me an example of a new idea or initiative you have suggested to your manager. How did you implement your idea?</div><span class="view">View ›</span></div>
      <div class="qi"><div class="q">2. Give me an example of a time when you made a mistake or didn't deliver on expectations, what happened? What did you learn?</div><span class="view">View ›</span></div>
      <div class="qi"><div class="q">3. How would your colleagues describe you in three words?</div><span class="view">View ›</span></div>
      <div class="qi"><div class="q">4. What parts of your current role frustate you?</div><span class="view">View ›</span></div>
      <div class="qi faded"><div class="q" style="font-weight:500">5. What steps would you take to make an important decision on the job?</div></div>
    </div>
  </div>

  <!-- Open question -->
  <div class="phone top" style="left:946px">
    <div class="status"><span>9:41</span><svg viewBox="0 0 24 5"><rect x="0" y="3" width="1" height="2" fill="#2b3445"/><rect x="1.6" y="2" width="1" height="3" fill="#2b3445"/><rect x="3.2" y="1" width="1" height="4" fill="#2b3445"/><rect x="4.8" y="0" width="1" height="5" fill="#2b3445"/><path d="M8.5 2a4 4 0 0 1 5 0M9.5 3.2a2.3 2.3 0 0 1 3 0" stroke="#2b3445" stroke-width=".7" fill="none"/><rect x="16" y=".5" width="6.5" height="4" rx="1" stroke="#2b3445" stroke-width=".5" fill="none"/><rect x="16.8" y="1.2" width="4.8" height="2.6" fill="#2b3445"/></svg></div>
    <div class="bar"><svg class="i" viewBox="0 0 10 10"><path d="M9 5H1.5M5 1.5 1.5 5 5 8.5" stroke="currentColor" stroke-width="1.3" fill="none"/></svg><span class="pill-title">View Questions &amp; Responses</span><svg class="bm" viewBox="0 0 8 10"><path d="M1 0h6v10L4 7.5 1 10z" fill="currentColor"/></svg></div>
    <div class="head"><div class="ico" role="img" aria-label="Behavioural category icon"></div>Behavioural</div>
    <div class="gray fill">
      <div class="sortzone"><span class="sort">Sort by ⌄</span></div>
      <div class="open">
        <div class="nav">←<br>PREV</div>
        <div class="open-mid"><div class="q">1. Give me an example of a new idea or initiative you have suggested to your manager. How did you implement your idea?</div><span class="chip" style="margin-top:5px">&lt; Share</span></div>
        <div class="nav next">→<br>NEXT</div>
      </div>
      <div class="resp"><div class="resp-h">Response 1<svg viewBox="0 0 8 10"><path d="M1 0h6v10L4 7.5 1 10z" fill="currentColor"/></svg></div><div class="tick"></div><p>I was attracted to this organisation because of the culture and what I have read on Staffvoice Reviews. I was very impressed</p></div>
      <div class="resp"><div class="resp-h">Response 2<svg viewBox="0 0 8 10"><path d="M1 0h6v10L4 7.5 1 10z" fill="currentColor"/></svg></div><div class="tick"></div><p>I was attracted to this organisation because of the culture and what I have read on Staffvoice Reviews. I was very impressed</p></div>
      <div class="resp"><div class="resp-h">Response 3<svg viewBox="0 0 8 10"><path d="M1 0h6v10L4 7.5 1 10z" fill="currentColor"/></svg></div><div class="tick"></div><p>I was attracted to this organisation because of the culture and what I have read on Staffvoice Reviews. I was very impressed</p></div>
    </div>
  </div>

  <!-- Interview tips selection -->
  <div class="phone bottom" style="left:81px">
    <div class="status"><span>9:41</span><svg viewBox="0 0 24 5"><rect x="18" y="3" width="1" height="2" fill="#2b3445"/><rect x="19.6" y="2" width="1" height="3" fill="#2b3445"/><rect x="21.2" y="1" width="1" height="4" fill="#2b3445"/><rect x="22.8" y="0" width="1" height="5" fill="#2b3445"/></svg></div>
    <div class="bar"><svg class="i" viewBox="0 0 10 10"><path d="M9 5H1.5M5 1.5 1.5 5 5 8.5" stroke="currentColor" stroke-width="1.3" fill="none"/></svg><span class="pill-title">Interview tips</span><span class="ghost"></span></div>
    <div class="gray fill">
      <div class="hint" style="padding-top:16px">Select your Interview Tip category</div>
      <div class="row"><div class="ico" role="img" aria-label="Checklist icon"></div><div class="row-txt"><div class="row-t">Tips for before the interview</div><div class="row-d">Pellentesque quis neque ut sapien fringilla iaculis ege inc...</div></div></div>
      <div class="row"><div class="ico" role="img" aria-label="Meeting icon"></div><div class="row-txt"><div class="row-t">Tips for during the interview</div><div class="row-d">Pellentesque quis neque ut sapien fringilla iaculis ege inc...</div></div></div>
      <div class="row"><div class="ico" role="img" aria-label="Light bulb icon"></div><div class="row-txt"><div class="row-t">Tips for after the interview</div><div class="row-d">Pellentesque quis neque ut sapien fringilla iaculis ege inc...</div></div></div>
      <div class="sec-h" style="padding-top:22px">Most searched</div>
      <div class="card">
        <div class="meta">View questions &amp; responses • Behavioural</div>
        <div class="q">Give me an example of a new idea or initiative you have suggested to your manager. How did you implement your idea?</div>
        <div class="chips"><span class="chip save"><svg viewBox="0 0 8 10"><path d="M1 0h6v10L4 7.5 1 10z" fill="#2b3445"/></svg>23 Saves</span><span class="chip">&lt; Share</span></div>
      </div>
      <div class="card">
        <div class="meta">View questions &amp; responses • Behavioural</div>
        <div class="q" style="font-weight:500">Give me an example of a new idea or initiative you have suggested to your manager. How did you implement your idea?</div>
        <div class="chips faded"><span class="chip save">23 Saves</span><span class="chip">&lt; Share</span></div>
      </div>
    </div>
  </div>

  <!-- View hints list -->
  <div class="phone bottom" style="left:299px">
    <div class="status"><span>9:41</span><svg viewBox="0 0 24 5"><rect x="16" y="3" width="1" height="2" fill="#2b3445"/><rect x="17.6" y="2" width="1" height="3" fill="#2b3445"/><rect x="19.2" y="1" width="1" height="4" fill="#2b3445"/><path d="M21 2a2.5 2.5 0 0 1 3 0" stroke="#2b3445" stroke-width=".7" fill="none"/></svg></div>
    <div class="bar"><svg class="i" viewBox="0 0 10 10"><path d="M6.5 1.5 3 5l3.5 3.5" stroke="currentColor" stroke-width="1.3" fill="none"/></svg><span class="pill-title">Interview tips</span><span class="ghost"></span></div>
    <div class="head"><div class="ico" role="img" aria-label="Checklist icon"></div>Tips for before the interview</div>
    <div class="gray fill">
      <div class="sortzone"><span class="sort">Sort by ⌄</span></div>
      <div class="qi"><div class="q">1. Start by researching the company and your interviewers</div><span class="view">View ›</span></div>
      <div class="qi"><div class="q">2. Give me an example of a time when you made a mistake or didn't deliver on expectations, what happened? What did you learn?</div><span class="view">View ›</span></div>
      <div class="qi"><div class="q">3. How would your colleagues describe you in three words?</div><span class="view">View ›</span></div>
      <div class="qi"><div class="q">4. What parts of your current role frustate you?</div><span class="view">View ›</span></div>
      <div class="qi faded"><div class="q" style="font-weight:500">5. What steps would you take to make an important decision on the job?</div></div>
    </div>
  </div>

  <!-- Hint 7 -->
  <div class="phone bottom" style="left:514px;top:704px">
    <div class="status"><span>9:41</span><svg viewBox="0 0 24 5"><rect x="0" y="3" width="1" height="2" fill="#2b3445"/><rect x="1.6" y="2" width="1" height="3" fill="#2b3445"/><rect x="3.2" y="1" width="1" height="4" fill="#2b3445"/><rect x="4.8" y="0" width="1" height="5" fill="#2b3445"/><path d="M8.5 2a4 4 0 0 1 5 0M9.5 3.2a2.3 2.3 0 0 1 3 0" stroke="#2b3445" stroke-width=".7" fill="none"/><rect x="16" y=".5" width="6.5" height="4" rx="1" stroke="#2b3445" stroke-width=".5" fill="none"/><rect x="16.8" y="1.2" width="4.8" height="2.6" fill="#2b3445"/></svg></div>
    <div class="bar"><svg class="i" viewBox="0 0 10 10"><path d="M9 5H1.5M5 1.5 1.5 5 5 8.5" stroke="currentColor" stroke-width="1.3" fill="none"/></svg><span class="pill-title">View Questions &amp; Responses</span><svg class="bm" viewBox="0 0 8 10"><path d="M1 0h6v10L4 7.5 1 10z" fill="currentColor"/></svg></div>
    <div class="head"><div class="ico" role="img" aria-label="Behavioural category icon"></div>Behavioural</div>
    <div class="gray fill">
      <div class="sortzone"><span class="sort">Sort by ⌄</span></div>
      <div class="open">
        <div class="nav">←<br>PREV</div>
        <div class="open-mid"><div class="q">7. Be prepared with examples of your work</div><span class="chip" style="margin-top:5px">&lt; Share</span></div>
        <div class="nav next">→<br>NEXT</div>
      </div>
      <div class="resp"><div class="resp-h">Tips<svg viewBox="0 0 8 10"><path d="M1 0h6v10L4 7.5 1 10z" fill="currentColor"/></svg></div><div class="tick"></div><p>During the interview, you Will likely be asked about specific work you've completed in relation to the position. After reviewing the job description, think of work you've done in past Jobs, clubs or volunteer positions that show you have experience and success doing the work they require</p></div>
    </div>
  </div>

  <!-- My collections -->
  <div class="phone bottom" style="left:731px">
    <div class="status"><span>9:41</span><svg viewBox="0 0 24 5"><rect x="0" y="3" width="1" height="2" fill="#2b3445"/><rect x="1.6" y="2" width="1" height="3" fill="#2b3445"/><rect x="3.2" y="1" width="1" height="4" fill="#2b3445"/><rect x="4.8" y="0" width="1" height="5" fill="#2b3445"/><path d="M8.5 2a4 4 0 0 1 5 0M9.5 3.2a2.3 2.3 0 0 1 3 0" stroke="#2b3445" stroke-width=".7" fill="none"/><rect x="16" y=".5" width="6.5" height="4" rx="1" stroke="#2b3445" stroke-width=".5" fill="none"/><rect x="16.8" y="1.2" width="4.8" height="2.6" fill="#2b3445"/></svg></div>
    <div class="bar"><svg class="i" viewBox="0 0 10 10"><path d="M9 5H1.5M5 1.5 1.5 5 5 8.5" stroke="currentColor" stroke-width="1.3" fill="none"/></svg><span class="pill-title">My collections</span><span class="ghost"></span></div>
    <div class="search wide"><svg viewBox="0 0 10 10"><circle cx="4" cy="4" r="3" stroke="currentColor" stroke-width="1.3" fill="none"/><path d="M6.3 6.3 9 9" stroke="currentColor" stroke-width="1.3"/></svg>Search in this section</div>
    <div class="gray fill" style="margin-top:8px">
      <div class="sortzone"><span class="sort">All categories ⌄</span></div>
      <div class="card" style="margin-top:0"><div class="meta">View questions &amp; responses • Behavioural</div><div class="q">4. What parts of your current role frustate you?</div><div class="chips"><span class="chip del">Delete this</span><span class="chip">View ›</span></div></div>
      <div class="card"><div class="meta">View questions &amp; responses • Behavioural</div><div class="q">3. How would your colleagues describe you in three words?</div><div class="chips"><span class="chip del">Delete this</span><span class="chip">View ›</span></div></div>
      <div class="card"><div class="meta">Interview tips • Tips before interview</div><div class="q">5. Recruit a friend to practice answering questions</div><div class="chips"><span class="chip del">Delete this</span><span class="chip">View ›</span></div></div>
      <div class="card"><div class="meta">Interview tips • Tips before interview</div><div class="q" style="font-weight:500">2. Practice your answers to common interview questions</div><div class="chips faded"><span class="chip del">Delete this</span><span class="chip">View ›</span></div></div>
    </div>
  </div>

  <!-- Search -->
  <div class="phone bottom" style="left:948px">
    <div class="status"><span>9:41</span><svg viewBox="0 0 24 5"><rect x="0" y="3" width="1" height="2" fill="#2b3445"/><rect x="1.6" y="2" width="1" height="3" fill="#2b3445"/><rect x="3.2" y="1" width="1" height="4" fill="#2b3445"/><rect x="4.8" y="0" width="1" height="5" fill="#2b3445"/><path d="M8.5 2a4 4 0 0 1 5 0M9.5 3.2a2.3 2.3 0 0 1 3 0" stroke="#2b3445" stroke-width=".7" fill="none"/><rect x="16" y=".5" width="6.5" height="4" rx="1" stroke="#2b3445" stroke-width=".5" fill="none"/><rect x="16.8" y="1.2" width="4.8" height="2.6" fill="#2b3445"/></svg></div>
    <div class="bar"><svg class="i" viewBox="0 0 10 10"><path d="M9 5H1.5M5 1.5 1.5 5 5 8.5" stroke="currentColor" stroke-width="1.3" fill="none"/></svg><span class="pill-title" style="padding:4px 14px">Search</span><span class="ghost"></span></div>
    <div class="search wide"><svg viewBox="0 0 10 10"><circle cx="4" cy="4" r="3" stroke="currentColor" stroke-width="1.3" fill="none"/><path d="M6.3 6.3 9 9" stroke="currentColor" stroke-width="1.3"/></svg>Search in this section</div>
    <div class="gray fill" style="margin-top:8px">
      <div class="empty-art" role="img" aria-label="Illustration of a person working on a laptop at a desk"></div>
      <div class="empty-t">Anything good starts with a good questions</div>
    </div>
  </div>

  <div class="label" style="left:52px;top:625px">Landing Screen</div>
  <div class="label" style="left:266px;top:625px">Menu Screen</div>
  <div class="label" style="left:484px;top:617px">Views questions<br><span class="sub">Selection Menú</span></div>
  <div class="label" style="left:698px;top:617px">Views questions<br><span class="sub">View list</span></div>
  <div class="label" style="left:913px;top:617px">Views questions<br><span class="sub">Open question</span></div>

  <div class="label" style="left:48px;top:1101px">Interview Tips<br><span class="sub">Selection Menú</span></div>
  <div class="label" style="left:270px;top:1101px">View Hints and Tips</div>
  <div class="label" style="left:475px;top:1101px">View Hints and Tips - Hint 7</div>
  <div class="label" style="left:698px;top:1098px">My question Portfolio<br>Saved Responses</div>
  <div class="label" style="left:915px;top:1098px">Search section</div>

</div>
</body>
</html>
```